Social Media Graphics - ALL TEXT RK

We are looking for a series of social media graphics for Instagram (standard size 1:1 (1080x1080px) that are ALL TEXT. We want the following quotes below on each graphic; one quote per graphic. AND, In very small letters at the bottom of each graphic, add @RKMarlowLive

The look and feel of these graphics should be complimentary to the color palette attached below; but keep them simple. But the design is up to you; at the end of this document, I provided various samples of all text graphics that I like as examples.

Target Market(s)

women looking to lose weight

Industry/Entity Type

health and wellness

Colors
E54698
E96AAD
F1A4CE
F9D9EA
FCEFF6

Requirements
Must have
• the quotes in the document
Should not have
• no stock photography

```html
<!DOCTYPE html>
<html lang="en">
<head>
<meta charset="utf-8">
<title>Stubborn Belly Fat Quote</title>
<link rel="stylesheet" href="https://fonts.googleapis.com/css2?family=Montserrat:wght@900&family=Roboto:wght@700&display=swap">
<style>
  :root {
    --pink-top: #ff0a84;
    --pink-mid: #ff5aa6;
    --pink-bottom: #fd9fcb;
    --text-white: #ffffff;
    --shadow-pink: #f58fc0;
  }
  html, body {
    margin: 0;
    padding: 0;
    width: 1200px;
    height: 1200px;
    overflow: hidden;
  }
  .quote-card {
    position: relative;
    width: 1200px;
    height: 1200px;
    background: linear-gradient(180deg, var(--pink-top) 0%, var(--pink-mid) 50%, var(--pink-bottom) 78%, var(--pink-bottom) 100%);
    display: flex;
    flex-direction: column;
    align-items: center;
  }
  .quote-text {
    position: absolute;
    top: 325px;
    left: 0;
    right: 0;
    margin: 0;
    text-align: center;
    font-family: "Montserrat", sans-serif;
    font-weight: 900;
    font-size: 77px;
    line-height: 98px;
    letter-spacing: 1px;
    text-transform: uppercase;
    color: var(--text-white);
    text-shadow: 4px 5px 0 var(--shadow-pink);
  }
  .handle {
    position: absolute;
    top: 808px;
    left: 0;
    right: 0;
    margin: 0;
    text-align: center;
    font-family: "Roboto", sans-serif;
    font-weight: 700;
    font-size: 31px;
    letter-spacing: 0.5px;
    text-transform: uppercase;
    color: var(--text-white);
  }
</style>
</head>
<body>
  <main class="quote-card">
    <h1 class="quote-text">That stubborn belly<br>fat isn't your fault -<br>here's what no one<br>tells you.</h1>
    <p class="handle">@RKMarlowLive</p>
  </main>
</body>
</html>
```